Visitenkarten für Goldankauf
Zielgruppe
wir sind fokussiert auf den Goldankauf
Aufgabenstellung
es soll elegant aber auch bisschen auffällig sein. aber nichts verspieltes
es heißt die Brennecks Wertecke
logo habe ich nicht

```html
<!DOCTYPE html>
<html lang="de">
<head>
<meta charset="utf-8">
<title>Brennecks Wertecke – Visitenkarten</title>
<link href="https://fonts.googleapis.com/css2?family=Quicksand:wght@300;500;600&display=swap" rel="stylesheet">
<style>
  :root {
    --bg: #dcdcdc;
    --card-black: #1c1c1c;
    --gold: #d4b06a;
    --gold-yellow: #f0cf45;
    --peach: #eeb27d;
    --paper: #f7f7f7;
    --ink-light: #f2f2f2;
  }
  * { margin: 0; padding: 0; box-sizing: border-box; }
  html, body { width: 1200px; height: 898px; overflow: hidden; }
  body {
    background: var(--bg);
    font-family: "Quicksand", sans-serif;
    position: relative;
  }
  .card {
    position: absolute;
    width: 540px;
    height: 300px;
    background: var(--card-black);
    overflow: hidden;
    box-shadow: 0 6px 18px rgba(0,0,0,.18);
  }
  .card--back { left: 40px; top: 299px; }
  .card--front { left: 620px; top: 299px; }

  .back-brand {
    position: absolute;
    right: 34px;
    bottom: 34px;
    display: flex;
    align-items: center;
    gap: 10px;
  }
  .brand-dot {
    width: 26px; height: 26px;
    border: 2px solid var(--gold);
    border-radius: 50%;
  }
  .brand-name {
    color: var(--gold);
    font-weight: 500;
    font-size: 19px;
    letter-spacing: .5px;
  }

  .front-art { position: absolute; inset: 0; }
  .front-mark {
    position: absolute;
    left: 330px; top: 58px;
    width: 200px;
    text-align: center;
    color: var(--gold);
    font-weight: 500;
    font-size: 24px;
    line-height: 1.2;
  }
  .wordmark {
    position: absolute;
    left: 30px; top: 36px;
  }
  .wordmark-name {
    color: var(--ink-light);
    font-weight: 300;
    font-size: 30px;
    letter-spacing: 1px;
    line-height: 1;
  }
  .wordmark-sub {
    color: var(--gold);
    font-weight: 500;
    font-size: 8px;
    letter-spacing: 3px;
    text-align: right;
    margin-top: 3px;
    padding-bottom: 5px;
    border-bottom: 1px solid var(--gold);
  }
  .address {
    position: absolute;
    left: 30px; top: 150px;
    color: var(--ink-light);
    font-weight: 600;
    font-size: 13px;
    line-height: 1.3;
  }
  .contacts {
    position: absolute;
    left: 30px; top: 196px;
    list-style: none;
    color: var(--ink-light);
    font-weight: 600;
    font-size: 13px;
  }
  .contacts li {
    display: flex;
    align-items: center;
    gap: 9px;
    height: 19px;
  }
  .contacts svg { width: 12px; height: 12px; fill: var(--gold); flex: none; }
</style>
</head>
<body>

  <section class="card card--back" aria-label="Rückseite">
    <div class="back-brand">
      <span class="brand-dot"></span>
      <span class="brand-name">Brennecks Wertecke</span>
    </div>
  </section>

  <section class="card card--front" aria-label="Vorderseite">
    <svg class="front-art" viewBox="0 0 540 300" width="540" height="300">
      <circle cx="430" cy="112" r="212" fill="var(--gold-yellow)"/>
      <circle cx="436" cy="106" r="200" fill="var(--peach)"/>
      <circle cx="450" cy="96" r="178" fill="var(--paper)"/>
    </svg>
    <div class="front-mark">Brennecks<br>Wertecke</div>

    <div class="wordmark">
      <div class="wordmark-name">Brennecks</div>
      <div class="wordmark-sub">WERTECKE</div>
    </div>

    <p class="address">Lindenhofweg 14<br>80997 Munich</p>

    <ul class="contacts">
      <li>
        <svg viewBox="0 0 24 24"><path d="M6.6 10.8a15 15 0 0 0 6.6 6.6l2.2-2.2c.3-.3.7-.4 1-.2 1.1.4 2.3.6 3.6.6.6 0 1 .4 1 1V20c0 .6-.4 1-1 1A17 17 0 0 1 3 4c0-.6.4-1 1-1h3.5c.6 0 1 .4 1 1 0 1.3.2 2.5.6 3.6.1.3 0 .7-.2 1z"/></svg>
        089412239056
      </li>
      <li>
        <svg viewBox="0 0 24 24"><path d="M7 1h10a2 2 0 0 1 2 2v18a2 2 0 0 1-2 2H7a2 2 0 0 1-2-2V3a2 2 0 0 1 2-2zm0 3v13h10V4zm5 15a1.2 1.2 0 1 0 0 2.4 1.2 1.2 0 0 0 0-2.4z"/></svg>
        01527730461
      </li>
      <li>
        <svg viewBox="0 0 24 24"><path d="M2 5h20v14H2zm2 2v.5l8 5 8-5V7zm0 2.8V17h16V9.8l-8 5z"/></svg>
        kontakt@isar-edelankauf.de
      </li>
      <li>
        <svg viewBox="0 0 24 24"><path d="M12 2a10 10 0 1 0 0 20 10 10 0 0 0 0-20zm-1 17.9A8 8 0 0 1 4.1 11L9 16v1a2 2 0 0 0 2 2zm6.9-2.5A2 2 0 0 0 16 16h-1v-3a1 1 0 0 0-1-1H8v-2h2a1 1 0 0 0 1-1V7h2a2 2 0 0 0 2-2v-.4a8 8 0 0 1 2.9 12.8z"/></svg>
        www.isar-edelankauf.de
      </li>
    </ul>
  </section>

</body>
</html>
```